Printed Circuit Boards Company Brochure Design Project

We are seeking a design of a professional brochure for our company. The company will contain information on the attached documents. The audience will be our prospective customers who are buyers of our printed circuit boards. The brochure should have three languages namely, English, Chinese and Japanese. The brochure will contain some technical details information of our current manufacturing capability. The key message is we are an organization that embraces excellence and customer satisfaction is our number one priority. As to the color scheme, we are opened even though our logo attached is green which is made of printed circuit boards. I like to have the brochure put some emphasis on our "EXCELLENCE" concept.

I have uploaded a fourth file which contains the Chinese translation. I like the brochure to have three languages. I will enclose the Japanese version tomorrow. Thanks. Arlo

I have posted an updated Japanese translation. Please incorporate Japanese into the design together with English and Chinese.  Use your imagination to present the brochure in a way that it is elegant to present the three languages. The take away of our company is we are committed to be a "credible" printed circuit board suppliers, starting from single sided PCB to multilayered PCB. We would like the audience to "feel" safe to buy from us as we are credible to make sure they have the lowest risks of procuring from us.

I have updated new brochure file in English, Chinese and Japanese. The changes I made is to eliminate the service section and move the original service contents to product section below the double sided and multilayered printed circuit boards.

I need the technical capability information be handled as an insert.

The brochure should contain some pockets to allows us to put a name card and other presentation materials.

buyers of printed circuit boards

It Company

• three languages, namely English , Chinese and Japanese.

```html
<!DOCTYPE html>
<html lang="en">
<head>
<meta charset="utf-8">
<title>We Do Serious Business – Flyer</title>
<link href="https://fonts.googleapis.com/css2?family=Roboto+Condensed:wght@300;400;700&family=Noto+Serif+TC:wght@400&display=swap" rel="stylesheet">
<style>
  :root {
    --blue-deep: #1386c4;
    --blue-mid: #1e9bd6;
    --blue-light: #37b4e4;
    --headline: #e4e8ea;
    --text: #f2f7fa;
    --photo-sky: #c9d8cf;
    --photo-window: #8fb09a;
    --photo-suit: #2a3140;
    --photo-table: #7a4a33;
  }
  * { margin: 0; padding: 0; box-sizing: border-box; }
  html, body { width: 1200px; height: 800px; overflow: hidden; background: #ffffff; }
  .flyer { position: relative; width: 1200px; height: 800px; overflow: hidden; }
  .flyer__photo {
    position: absolute; left: 0; top: 0; width: 1200px; height: 390px;
    background:
      linear-gradient(180deg, rgba(255,255,255,0) 60%, rgba(122,74,51,0.45) 88%, var(--photo-table) 100%),
      linear-gradient(90deg, var(--photo-suit) 0%, #5f6f74 14%, var(--photo-window) 32%, var(--photo-sky) 50%, var(--photo-window) 68%, #4e5a66 86%, var(--photo-suit) 100%);
  }
  .flyer__band {
    position: absolute; left: 0; top: 390px; width: 1200px; height: 410px;
    background: linear-gradient(100deg, var(--blue-deep) 0%, var(--blue-mid) 55%, var(--blue-light) 100%);
    color: var(--text);
  }
  .headline {
    position: absolute; left: 80px; top: 70px;
    font-family: "Roboto Condensed", sans-serif; color: var(--headline);
    font-size: 100px; line-height: 0.82; letter-spacing: -7px; text-transform: uppercase;
  }
  .headline span { display: block; }
  .headline__light { font-weight: 300; }
  .headline__bold { font-weight: 700; letter-spacing: -6px; }
  .brace { position: absolute; top: 40px; width: 30px; height: 320px; }
  .brace--left { left: 470px; }
  .brace--right { left: 1120px; }
  .contact {
    position: absolute; font-family: "Roboto Condensed", sans-serif; font-style: normal;
    font-weight: 300; font-size: 15px; line-height: 21px; letter-spacing: -0.3px;
  }
  .contact__title { font-weight: 400; font-size: 17px; margin-bottom: 4px; }
  .contact__title--zh { font-family: "Noto Serif TC", serif; }
  .contact--zh { font-family: "Noto Serif TC", serif; font-size: 14px; }
  .contact--zh .contact__title { font-size: 17px; }
  .contact--hk-en { left: 520px; top: 22px; }
  .contact--cn-en { left: 520px; top: 210px; }
  .contact--hk-zh { left: 830px; top: 22px; }
  .contact--cn-zh { left: 830px; top: 210px; }
</style>
</head>
<body>
  <main class="flyer">
    <div class="flyer__photo" role="img" aria-label="Photo of a business team in suits meeting around a table by an office window"></div>

    <section class="flyer__band">
      <h1 class="headline">
        <span class="headline__light">We Do</span>
        <span class="headline__bold">Serious</span>
        <span class="headline__light">Business</span>
      </h1>

      <svg class="brace brace--left" viewBox="0 0 30 320" aria-hidden="true">
        <path d="M26 2 C12 2 14 20 14 60 L14 140 C14 152 10 158 3 160 C10 162 14 168 14 180 L14 260 C14 300 12 318 26 318" fill="none" stroke="#f2f7fa" stroke-width="2.5"/>
      </svg>
      <svg class="brace brace--right" viewBox="0 0 30 320" aria-hidden="true">
        <path d="M4 2 C18 2 16 20 16 60 L16 140 C16 152 20 158 27 160 C20 162 16 168 16 180 L16 260 C16 300 18 318 4 318" fill="none" stroke="#f2f7fa" stroke-width="2.5"/>
      </svg>

      <address class="contact contact--hk-en">
        <div class="contact__title contact__title--zh" lang="zh-Hant">香港聯絡辦事處:</div>
        Northwell Circuits Limited<br>
        18/F, Harbour Crest,<br>
        72 Marlow Road,<br>
        Quarry Point, Hong Kong<br>
        Telephone: (852)2400-1188<br>
        Fax: (852)2400-1199<br>
        Email: sales@northwellpcb.example
      </address>

      <address class="contact contact--cn-en">
        <div class="contact__title">China Factory</div>
        Northwell Circuits (Riverside) Limited<br>
        9 Linfeng East 3 Road,<br>
        138 Industrial District,<br>
        Heshan Town, Riverside,<br>
        Guangdong Province, China 510990<br>
        Telephone: (86)750-6600-2101<br>
        Fax: (86)750-6600-2102
      </address>

      <address class="contact contact--zh contact--hk-zh" lang="zh-Hant">
        <div class="contact__title">香港聯絡辦事處</div>
        北苑電路國際有限公司<br>
        香港石澳角<br>
        馬洛道七十二號<br>
        港灣峰十八樓<br>
        電話: (852) 2400-1188<br>
        傳真: (852)2400-1199<br>
        電郵: sales@northwellpcb.example
      </address>

      <address class="contact contact--zh contact--cn-zh" lang="zh-Hant">
        <div class="contact__title">中國工場</div>
        北苑電路(河畔)有限公司<br>
        中國廣東省河畔市<br>
        鶴山鎮138工業區<br>
        林峰東三路九號<br>
        郵編編號: 510990<br>
        電話: (86)750-6600-2101<br>
        傳真: (86)750-6600-2102
      </address>
    </section>
  </main>
</body>
</html>
```